I have a new startup... www.hirebybrindle.com
An issue Im running into is when people create profiles there banner images are getting messed up. So instead I would like anywhere to 10-15 banners created as stock banners for my site the people signing up need to choose from so the website looks more in uniform. The site contains graphic designers, photographers, & videographers so maybe some banners can be patterns of a camera outline or graphic design tools etc. Need really clean and sleek looking banners that these people can pick from that will make sense.
I will attach my logo if you want to do a cool "Brindle" pattern design as a banner.
Banner sizes 2000px by 560px.

If you have any questions please let me know.

```html
<!DOCTYPE html>
<html lang="en">
<head>
<meta charset="utf-8">
<title>Brindle profile banners</title>
<link href="https://fonts.googleapis.com/css2?family=Roboto:wght@300;400;900&family=Roboto+Condensed:wght@300;400;700&display=swap" rel="stylesheet">
<style>
  :root {
    --page-bg: #000000;
    --frame: #5a5a5a;
    --brand: #c8482a;
    --white: #ffffff;
    --soft-white: #e6e6e6;
    --muted: #cfcfcf;
  }
  * { margin: 0; padding: 0; box-sizing: border-box; }
  html, body {
    width: 1200px; height: 1091px; overflow: hidden;
    background: var(--page-bg);
  }
  .banner {
    position: absolute; left: 120px; width: 964px; height: 274px;
    border: 3px solid var(--frame);
    background: #000;
    overflow: hidden;
  }
  .banner--photo { top: 113px; }
  .banner--video { top: 415px; }
  .banner--design { top: 734px; }

  .banner__image {
    position: absolute; top: 0; right: 0; width: 640px; height: 100%;
    -webkit-mask-image: linear-gradient(90deg, transparent 0%, #000 55%);
            mask-image: linear-gradient(90deg, transparent 0%, #000 55%);
  }
  .banner--photo .banner__image {
    background: radial-gradient(ellipse at 80% 40%, #3a3a3c 0%, #1c1c1e 45%, #0b0b0c 80%);
  }
  .banner--video .banner__image {
    background: linear-gradient(120deg, #7a5a3a 0%, #4b4a5a 35%, #2a2d44 65%, #1c2036 100%);
    opacity: .85;
  }
  .banner--design .banner__image {
    background: linear-gradient(110deg, #3c2f22 0%, #5c5148 40%, #3e4b48 70%, #4a3a26 100%);
    opacity: .8;
  }
  .banner__glow {
    position: absolute; left: 0; top: 0; width: 700px; height: 100%;
    background:
      radial-gradient(ellipse 180px 60px at 440px 210px, rgba(200,72,42,.45), transparent 70%),
      radial-gradient(ellipse 120px 140px at 470px 80px, rgba(200,72,42,.3), transparent 70%),
      radial-gradient(ellipse 260px 50px at 150px 250px, rgba(200,72,42,.35), transparent 70%);
  }

  .brand {
    position: absolute; left: 45px; top: 47px;
    font: 900 74px/1 "Roboto", sans-serif;
    color: var(--brand);
    letter-spacing: -1px;
  }
  .headline {
    position: absolute; left: 45px; top: 132px;
    font: 300 36px/1 "Roboto", sans-serif;
    color: var(--white);
  }
  .subline {
    position: absolute; left: 45px; top: 177px;
    font: 400 29px/1 "Roboto Condensed", sans-serif;
    color: var(--white);
  }
  .cta {
    position: absolute; left: 40px; top: 218px; width: 392px; height: 36px;
    background: var(--brand);
    border-radius: 11px;
    box-shadow: 2px 2px 0 #000;
    padding-left: 21px;
    font: 700 22px/36px "Roboto Condensed", sans-serif;
    letter-spacing: 3px;
    color: var(--white);
  }
  .cta__pointer {
    position: absolute; left: 367px; top: 224px; width: 34px; height: 38px;
  }

  .role {
    position: absolute;
    color: var(--muted);
    white-space: nowrap;
  }
  .role--minor {
    font: 300 23px/1 "Roboto Condensed", sans-serif;
    letter-spacing: 6px;
  }
  .role--major {
    font: 300 53px/1 "Roboto Condensed", sans-serif;
    color: var(--white);
  }
  .role--top { left: 505px; top: 123px; }
  .role--main { left: 448px; top: 156px; }
  .role--bottom { left: 613px; top: 213px; }
  .banner--design .role--main { left: 458px; color: var(--soft-white); }
  .banner--design .role--bottom { left: 573px; letter-spacing: 10px; }
</style>
</head>
<body>

<section class="banner banner--photo">
  <div class="banner__image" role="img" aria-label="Photographer holding a camera to his eye"></div>
  <div class="banner__glow" role="img" aria-label="Orange light streaks"></div>
  <div class="brand">BRINDLE</div>
  <p class="headline">Find Creative Pros</p>
  <p class="subline">Work with local professionals.</p>
  <div class="cta">www.hirebybrindle.com</div>
  <svg class="cta__pointer" viewBox="0 0 34 38"><path d="M2 2 L2 30 L9 24 L15 36 L20 34 L14 22 L24 22 Z" fill="#fff" stroke="#000" stroke-width="1.5"/></svg>
  <p class="role role--minor role--top">VIDEOGRAPHERS</p>
  <p class="role role--major role--main">PHOTOGRAPHERS</p>
  <p class="role role--minor role--bottom">GRAPHIC DESIGNER</p>
</section>

<section class="banner banner--video">
  <div class="banner__image" role="img" aria-label="Videographer operating a film camera"></div>
  <div class="banner__glow" role="img" aria-label="Orange light streaks"></div>
  <div class="brand">BRINDLE</div>
  <p class="headline">Find Creative Pros</p>
  <p class="subline">Work with local professionals.</p>
  <div class="cta">www.hirebybrindle.com</div>
  <svg class="cta__pointer" viewBox="0 0 34 38"><path d="M2 2 L2 30 L9 24 L15 36 L20 34 L14 22 L24 22 Z" fill="#fff" stroke="#000" stroke-width="1.5"/></svg>
  <p class="role role--minor role--top">PHOTOGRAPHERS</p>
  <p class="role role--major role--main">VIDEOGRAPHERS</p>
  <p class="role role--minor role--bottom">GRAPHIC DESIGNER</p>
</section>

<section class="banner banner--design">
  <div class="banner__image" role="img" aria-label="Designer desk with laptop, camera and colour swatches"></div>
  <div class="banner__glow" role="img" aria-label="Orange light streaks"></div>
  <div class="brand">BRINDLE</div>
  <p class="headline">Find Creative Pros</p>
  <p class="subline">Work with local professionals.</p>
  <div class="cta">www.hirebybrindle.com</div>
  <svg class="cta__pointer" viewBox="0 0 34 38"><path d="M2 2 L2 30 L9 24 L15 36 L20 34 L14 22 L24 22 Z" fill="#fff" stroke="#000" stroke-width="1.5"/></svg>
  <p class="role role--minor role--top">PHOTOGRAPHERS</p>
  <p class="role role--major role--main">GRAPHIC DESIGNER</p>
  <p class="role role--minor role--bottom">VIDEOGRAPHERS</p>
</section>

</body>
</html>
```